Landing Page that will convert (Design Only Landing Page Project)

I am looking for a design that will resonate with a dentist, doctor or anyone business owner in the medical field. My goal is to have then scheduled a 15 min session with me at the end to discuss how I can help then meet there financial goals (short or long term)

I am open to all design concepts and suggestions as far as the important contents or links that should be on the page (ie. Main menu like, Home, About, Services, Schedule, Contact Us).

There is no right or wrong answer, just need a great accounting/financing landing page. Again the project is for just the design of the page, and coding will be done elsewhere.

Target Market(s)

medical professionals, this includes small business owners of privately held office suck as medical doctors, dentist, ophthalmologist, chiropractors, etc

Industry/Entity Type

Finance And Accounting

Colors
fdfdfd
1b1b1b
f3f1f8
e4daeb

Requirements
Must have
• The goal of this landing page is to have the visitor schedule a 15min discovery call, therefore, a calender scheduling option is ideal, so we can understand their goals and see what obstacles they are facing and therefore avoid those obstacles before they become a burden
Nice to have
• A video background or maybe a medical professional office in that way they feel connected. For design purposes just use a video/image placeholder. I feel more is less if we can research some of the most successful landing page design and incorporate some of those elements that would to great.
• I saw this example and thought it was ok
• https://www.plovanet.com/#features
• WHAT I LIKE ABOUT THIS DESIGN:
• - It's simple, clean,
• - font is readable,
• - like the illustration
• - elegance
• - It clearly defines what the use should do, its intuitive, walks the user to the bottom of the page and give them the option of whether to signup or exit the page.

```html
<!DOCTYPE html>
<html lang="en">
<head>
<meta charset="utf-8">
<title>Meridian Ledger – Financial Goals for Medical Practices</title>
<link href="https://fonts.googleapis.com/css2?family=Lato:wght@300;400;700&family=Oswald:wght@400;500&family=Philosopher:wght@700&family=Raleway:wght@400&display=swap" rel="stylesheet">
<style>
:root{
  --plum:#4a2b45;
  --plum-dark:#3a2036;
  --lavender:#e4daeb;
  --mist:#f3f1f8;
  --white:#fdfdfd;
  --ink:#1b1b1b;
  --grey:#8a8590;
  --footer:#f2f1f3;
}
*{box-sizing:border-box;margin:0;padding:0}
html,body{width:1200px;height:4045px;overflow:hidden}
body{position:relative;background:var(--white);font-family:'Lato',sans-serif;color:var(--ink)}
.abs{position:absolute}
p.body-copy{font-size:14px;line-height:26px;color:var(--grey)}
.btn{display:inline-block;background:var(--plum-dark);color:var(--white);font-family:'Lato',sans-serif;font-size:16px;text-transform:uppercase;border-radius:30px;padding:15px 34px;text-decoration:none}
.section-heading{font-family:'Oswald',sans-serif;font-weight:500;font-size:28px;line-height:44px;text-transform:uppercase;color:var(--plum-dark)}

/* header */
.top-band{left:0;top:0;width:1200px;height:200px;background:var(--plum)}
.brand{left:75px;top:34px;font-family:'Lato',sans-serif;font-weight:400;font-size:38px;color:var(--white);letter-spacing:.5px}
.main-nav{left:418px;top:46px;display:flex;gap:38px}
.main-nav a{color:var(--white);font-size:15px;text-decoration:none}
.nav-caret{left:428px;top:104px}
.nav-search{left:870px;top:48px}
.nav-phone{left:928px;top:42px;display:flex;align-items:center;gap:10px;color:var(--white);font-size:20px}

/* hero */
.hero-photo{left:208px;top:127px;width:917px;height:570px;
  background:
    radial-gradient(ellipse 30% 40% at 80% 30%,rgba(231,160,170,.75),transparent 70%),
    radial-gradient(ellipse 35% 30% at 62% 72%,rgba(226,170,150,.7),transparent 70%),
    radial-gradient(ellipse 25% 35% at 92% 80%,rgba(140,190,220,.7),transparent 70%),
    linear-gradient(135deg,#eef3f6 0%,#e6d3da 45%,#c7dbe6 100%)}
.hero-card{left:0;top:270px;width:540px;height:427px;background:rgba(253,253,253,.93);padding:70px 40px 0 80px}
.hero-title{font-family:'Philosopher',sans-serif;font-weight:700;font-size:50px;line-height:58px;color:var(--plum-dark)}
.hero-card p{font-size:15px;line-height:28px;color:var(--ink);margin-top:18px}
.hero-arrows{left:98px;top:228px}
.side-rail{left:1125px;top:200px;width:75px;height:497px;background:var(--white)}
.side-rail .dots{position:absolute;left:32px;top:52px;display:flex;flex-direction:column;gap:26px}
.side-rail .dots span{width:11px;height:11px;border-radius:50%;background:var(--plum)}
.side-rail .scroll{position:absolute;left:30px;top:360px;transform:rotate(-90deg);transform-origin:left top;font-size:12px;letter-spacing:1px;text-transform:uppercase;white-space:nowrap;color:var(--ink)}
.hero-band{left:0;top:697px;width:1200px;height:126px;background:var(--plum)}
.video-thumb{left:75px;top:594px;width:255px;height:166px;
  background:radial-gradient(ellipse 40% 50% at 30% 55%,rgba(150,135,120,.8),transparent 70%),
    radial-gradient(ellipse 30% 45% at 78% 50%,rgba(190,180,175,.6),transparent 70%),
    linear-gradient(135deg,#2f2d33,#5a555c 60%,#3e3a42)}
.play{left:168px;top:642px}
.hero-band-text{left:370px;top:728px;width:520px;font-size:15px;line-height:30px;color:var(--white)}
.btn-outline{left:914px;top:734px;width:208px;height:54px;border:1.5px solid var(--white);border-radius:30px;color:var(--white);font-size:15px;text-transform:uppercase;display:flex;align-items:center;justify-content:center}

/* about */
.about-title{left:0;top:868px;width:1200px;text-align:center;font-family:'Raleway',sans-serif;font-weight:400;font-size:38px;color:var(--ink)}
.about-frame{left:318px;top:950px;width:562px;height:383px;border:9px solid var(--plum-dark);border-radius:18px;box-shadow:0 8px 18px rgba(0,0,0,.18);
  background:
    radial-gradient(ellipse 22% 28% at 50% 50%,rgba(110,180,230,.85),transparent 70%),
    radial-gradient(ellipse 18% 22% at 52% 25%,rgba(235,150,110,.8),transparent 70%),
    radial-gradient(ellipse 40% 10% at 50% 80%,rgba(200,90,80,.55),transparent 70%),
    radial-gradient(ellipse 14% 16% at 80% 38%,rgba(245,200,120,.75),transparent 70%),
    radial-gradient(ellipse 14% 16% at 20% 40%,rgba(160,200,220,.75),transparent 70%),
    #ddd0ea}
.about-copy{left:195px;top:1370px;width:810px;text-align:center}
.about-btn{left:518px;top:1504px}

/* feature rows */
.band-lav{left:0;width:1200px;background:var(--lavender)}
.feature-frame{width:421px;height:348px;border-radius:24px;background:var(--white);box-shadow:0 4px 14px rgba(0,0,0,.15);padding:22px}
.feature-art{width:100%;height:100%;border-radius:12px}
.art-consult{background:
  radial-gradient(ellipse 18% 30% at 30% 45%,rgba(120,160,200,.7),transparent 70%),
  radial-gradient(ellipse 16% 30% at 72% 50%,rgba(110,180,120,.6),transparent 70%),
  radial-gradient(ellipse 12% 10% at 55% 20%,rgba(245,210,90,.7),transparent 70%),
  radial-gradient(ellipse 35% 12% at 40% 72%,rgba(120,95,75,.6),transparent 70%),
  #f7f6f8}
.art-calendar{background:
  radial-gradient(ellipse 30% 35% at 58% 52%,rgba(40,40,50,.8),transparent 70%),
  radial-gradient(ellipse 12% 35% at 35% 60%,rgba(245,200,60,.6),transparent 70%),
  radial-gradient(ellipse 12% 35% at 85% 60%,rgba(80,150,210,.6),transparent 70%),
  radial-gradient(ellipse 8% 25% at 15% 55%,rgba(200,220,235,.9),transparent 70%),
  #f9f8fa}
.art-meeting{background:
  radial-gradient(ellipse 25% 30% at 50% 55%,rgba(50,90,150,.7),transparent 70%),
  radial-gradient(ellipse 10% 10% at 20% 20%,rgba(70,130,200,.6),transparent 70%),
  radial-gradient(ellipse 10% 10% at 80% 25%,rgba(80,140,210,.6),transparent 70%),
  radial-gradient(ellipse 8% 8% at 58% 10%,rgba(245,190,60,.7),transparent 70%),
  radial-gradient(ellipse 9% 9% at 82% 80%,rgba(230,110,70,.6),transparent 70%),
  #f8f8fb}
.feature-text{width:560px}
.feature-text p{margin-top:16px}
.feature-text .btn{margin-top:28px}

/* schedule */
.schedule-title{left:75px;top:3120px;font-family:'Lato',sans-serif;font-weight:400;font-size:38px;color:var(--ink)}
.schedule-intro{left:75px;top:3188px;width:300px;font-size:14px;line-height:26px;color:var(--grey)}
.field{height:54px;border:1px solid #e6e3ea;background:var(--white);font-size:13px;font-style:italic;color:var(--grey);padding:0 14px;display:flex;align-items:center}
.submit{left:230px;top:3478px;width:140px;height:54px;background:var(--plum-dark);color:var(--white);font-size:17px;text-transform:uppercase;display:flex;align-items:center;justify-content:center}
.schedule-panel{left:545px;top:3148px;width:655px;height:472px;background:var(--plum)}
.schedule-photo{left:420px;top:3100px;width:520px;height:520px;border-radius:48% 52% 0 0 / 40% 40% 0 0;
  background:
    radial-gradient(ellipse 25% 22% at 62% 22%,rgba(210,160,130,.9),transparent 70%),
    radial-gradient(ellipse 22% 20% at 35% 32%,rgba(220,175,150,.85),transparent 70%),
    radial-gradient(ellipse 40% 30% at 50% 70%,rgba(250,250,250,.95),transparent 75%),
    radial-gradient(ellipse 30% 20% at 60% 95%,rgba(70,100,150,.6),transparent 70%),
    linear-gradient(160deg,#b89a80 0%,#ece6e0 45%,#d8d0de 100%)}
.panel-brand{left:965px;top:3196px;font-size:22px;color:var(--white)}

/* footer */
.footer{left:0;top:3620px;width:1200px;height:345px;background:var(--footer)}
.foot-col{top:3660px;width:230px}
.foot-col h4{font-family:'Lato',sans-serif;font-weight:400;font-size:20px;color:var(--ink);margin-bottom:20px}
.foot-col p,.foot-col li{font-size:13px;line-height:24px;color:#6b6670;list-style:none}
.foot-col a{color:var(--plum-dark);font-weight:700}
.contact-row{display:flex;gap:14px;margin-bottom:10px}
.contact-row strong{color:var(--ink)}
.newsletter-box{margin-top:14px;width:240px;height:60px;border-radius:30px;background:var(--white);box-shadow:0 2px 8px rgba(0,0,0,.12);display:flex;align-items:center;justify-content:space-between;padding:0 4px 0 22px;font-size:13px;font-style:italic;color:var(--grey)}
.send{width:52px;height:52px;border-radius:50%;background:var(--plum-dark);display:flex;align-items:center;justify-content:center}
.bottom-bar{left:0;top:3965px;width:1200px;height:80px;background:var(--plum);color:var(--white);font-size:13px;display:flex;align-items:center;justify-content:space-between;padding:0 75px 0 75px}
.social{display:flex;gap:10px;margin-right:15px}
.social span{width:36px;height:36px;border:1.5px solid var(--white);border-radius:50%;display:flex;align-items:center;justify-content:center}
.social span::after{content:"";width:10px;height:10px;border-radius:50%;background:var(--white)}
</style>
</head>
<body>

<!-- header -->
<div class="abs top-band"></div>
<div class="abs brand">meridian ledger</div>
<nav class="abs main-nav"><a href="#">Home</a><a href="#">About</a><a href="#">Services</a><a href="#">Schedule</a><a href="#">Contact Us</a></nav>
<svg class="abs nav-caret" width="16" height="10"><path d="M0 10 L8 2 L16 10Z" fill="#fdfdfd"/></svg>
<svg class="abs nav-search" width="20" height="20" fill="none" stroke="#fdfdfd" stroke-width="2"><circle cx="8" cy="8" r="6"/><path d="M12.5 12.5 L18 18"/></svg>
<div class="abs nav-phone">
  <svg width="26" height="26" viewBox="0 0 24 24" fill="#fdfdfd"><path d="M6.6 10.8a15 15 0 0 0 6.6 6.6l2.2-2.2a1 1 0 0 1 1-.25 11.4 11.4 0 0 0 3.6.6 1 1 0 0 1 1 1V20a1 1 0 0 1-1 1A17 17 0 0 1 3 4a1 1 0 0 1 1-1h3.5a1 1 0 0 1 1 1c0 1.25.2 2.45.6 3.6a1 1 0 0 1-.25 1z"/></svg>
  <span>+1.555.010.2400</span>
</div>

<!-- hero -->
<div class="abs hero-photo" role="img" aria-label="Photo of a dentist treating a smiling patient in a bright clinic"></div>
<svg class="abs hero-arrows" width="90" height="20" fill="none" stroke="#1b1b1b" stroke-width="2"><path d="M30 10H4M11 3L4 10l7 7"/><path d="M58 10h26M77 3l7 7-7 7" stroke="#8a8590"/></svg>
<div class="abs hero-card">
  <h1 class="hero-title">Meridian Ledger<br>Financial Goals</h1>
  <p>Lorem ipsum dolor sit amet, consectetur adipiscing elit, sed do eiusmod tempor incididunt ut labore et dolore magna aliqua.</p>
</div>
<div class="abs side-rail">
  <div class="dots"><span></span><span></span><span></span></div>
  <span class="scroll">Scroll Down</span>
</div>
<div class="abs hero-band"></div>
<div class="abs video-thumb" role="img" aria-label="Video placeholder showing a medical office team"></div>
<svg class="abs play" width="68" height="68"><circle cx="34" cy="34" r="31" fill="none" stroke="#fdfdfd" stroke-width="2.5"/><path d="M28 22 L46 34 L28 46Z" fill="#fdfdfd"/></svg>
<p class="abs hero-band-text">Lorem ipsum dolor sit amet, consectetur adipiscing elit, sed do eiusmod tempor incididunt ut labore et dolore magna aliqua.</p>
<div class="abs btn-outline">Book Appointment</div>

<!-- about -->
<h2 class="abs about-title">About Meridian Ledger</h2>
<div class="abs about-frame" role="img" aria-label="Illustration of an accountant multitasking at a desk with charts and coins"></div>
<p class="abs body-copy about-copy">Lorem ipsum dolor sit amet, consectetur adipiscing elit, sed do eiusmod tempor incididunt ut labore et dolore magna aliqua. Ut enim ad minim veniam, quis nostrud exercitation ullamco laboris nisi ut aliquip ex ea commodo consequat. Duis aute irure dolor in reprehenderit in voluptate velit esse cillum dolore eu fugiat nulla pariatur. Excepteur sint occaecat cupidatat non proident, sunt in culpa qui officia deserunt mollit anim id est laborum.</p>
<a class="abs btn about-btn" href="#">Read More</a>

<!-- feature 1 -->
<div class="abs band-lav" style="top:1618px;height:478px"></div>
<div class="abs feature-frame" style="left:75px;top:1675px"><div class="feature-art art-consult" role="img" aria-label="Illustration of a doctor consulting a patient across a desk"></div></div>
<div class="abs feature-text" style="left:564px;top:1676px">
  <h3 class="section-heading">The goals is to have the visitor schedule a 15min discovery call</h3>
  <p class="body-copy">Lorem ipsum dolor sit amet, consectetur adipiscing elit, sed do eiusmod tempor incididunt ut labore et dolore magna aliqua. Ut enim ad minim veniam, quis nostrud exercitation ullamco laboris nisi ut aliquip ex ea commodo consequat. Duis aute irure dolor in reprehenderit in voluptate velit esse cillum dolore eu fugiat nulla pariatur. Excepteur sint occaecat cupidatat non proident, sunt in culpa qui officia deserunt mollit anim id est laborum.</p>
  <a class="btn" href="#">Read More</a>
</div>

<!-- feature 2 -->
<div class="abs feature-text" style="left:75px;top:2152px">
  <h3 class="section-heading">A calender scheduling option is ideal, so we can understand their goals</h3>
  <p class="body-copy">Lorem ipsum dolor sit amet, consectetur adipiscing elit, sed do eiusmod tempor incididunt ut labore et dolore magna aliqua. Ut enim ad minim veniam, quis nostrud exercitation ullamco laboris nisi ut aliquip ex ea commodo consequat. Duis aute irure dolor in reprehenderit in voluptate velit esse cillum dolore eu fugiat nulla pariatur. Excepteur sint occaecat cupidatat non proident, sunt in culpa qui officia deserunt mollit anim id est laborum.</p>
  <a class="btn" href="#">Read More</a>
</div>
<div class="abs feature-frame" style="left:704px;top:2155px"><div class="feature-art art-calendar" role="img" aria-label="Illustration of a doctor beside a calendar screen"></div></div>

<!-- feature 3 -->
<div class="abs band-lav" style="top:2565px;height:477px"></div>
<div class="abs feature-frame" style="left:75px;top:2623px"><div class="feature-art art-meeting" role="img" aria-label="Illustration of two business people meeting surrounded by planning icons"></div></div>
<div class="abs feature-text" style="left:564px;top:2628px">
  <h3 class="section-heading">See what obstacles they are facing and therefore avoid those obstacles before they become a burden</h3>
  <p class="body-copy">Lorem ipsum dolor sit amet, consectetur adipiscing elit, sed do eiusmod tempor incididunt ut labore et dolore magna aliqua. Ut enim ad minim veniam, quis nostrud exercitation ullamco laboris nisi ut aliquip ex ea commodo consequat. Duis aute irure dolor in reprehenderit in voluptate velit esse cillum dolore.</p>
  <a class="btn" href="#">Read More</a>
</div>

<!-- schedule -->
<h2 class="abs schedule-title">Schedule</h2>
<p class="abs schedule-intro">Lorem ipsum dolor sit amet, consectetur adipiscing elit, sed do eiusmod tempor incididunt ut labore et dolore magna aliqua.</p>
<div class="abs field" style="left:75px;top:3290px;width:295px">Name :</div>
<div class="abs field" style="left:75px;top:3352px;width:142px">Email :</div>
<div class="abs field" style="left:228px;top:3352px;width:142px">Phone :</div>
<div class="abs field" style="left:75px;top:3414px;width:295px">Subject :</div>
<div class="abs field" style="left:75px;top:3478px;width:142px;justify-content:space-between">Date :
  <svg width="16" height="16" fill="none" stroke="#8a8590" stroke-width="1.5"><rect x="1.5" y="3" width="13" height="11.5"/><path d="M1.5 7h13M5 1v4M11 1v4"/></svg>
</div>
<div class="abs submit">Submit Now</div>
<div class="abs schedule-panel"></div>
<div class="abs schedule-photo" role="img" aria-label="Photo of a smiling family taking a selfie together"></div>
<div class="abs panel-brand">meridian ledger</div>

<!-- footer -->
<div class="abs footer"></div>
<div class="abs foot-col" style="left:75px">
  <h4>About Us</h4>
  <p>Lorem ipsum dolor sit amet, consectetur adipiscing elit, sed do eiusmod tempor incididunt ut labore et dolore <a href="#">READ MORE</a></p>
</div>
<div class="abs foot-col" style="left:348px">
  <h4>Useful Links</h4>
  <ul><li>Home</li><li>About</li><li>Services</li><li>Schedule</li><li>Contact Us</li></ul>
</div>
<div class="abs foot-col" style="left:615px;width:250px">
  <h4>Get In Touch</h4>
  <div class="contact-row">
    <svg width="14" height="18" viewBox="0 0 14 18"><path d="M7 0a7 7 0 0 1 7 7c0 5-7 11-7 11S0 12 0 7a7 7 0 0 1 7-7z" fill="#3a2036"/><circle cx="7" cy="7" r="2.5" fill="#f2f1f3"/></svg>
    <p><strong>Meridian Ledger</strong><br>123, Address, State Name<br>City, Street, Zipcode</p>
  </div>
  <div class="contact-row">
    <svg width="14" height="14" viewBox="0 0 24 24" fill="#3a2036"><path d="M6.6 10.8a15 15 0 0 0 6.6 6.6l2.2-2.2a1 1 0 0 1 1-.25 11.4 11.4 0 0 0 3.6.6 1 1 0 0 1 1 1V20a1 1 0 0 1-1 1A17 17 0 0 1 3 4a1 1 0 0 1 1-1h3.5a1 1 0 0 1 1 1c0 1.25.2 2.45.6 3.6a1 1 0 0 1-.25 1z"/></svg>
    <p>+1.555.010.2400</p>
  </div>
  <div class="contact-row">
    <svg width="16" height="12" fill="none" stroke="#3a2036" stroke-width="1.6"><rect x="1" y="1" width="14" height="10"/><path d="M1 1l7 6 7-6"/></svg>
    <p>info@meridianledger.com</p>
  </div>
</div>
<div class="abs foot-col" style="left:885px;width:250px">
  <h4>Newsletter</h4>
  <p>Would you like to receive exclusive access to articles, white papers and our regular monthly newsletter?</p>
  <div class="newsletter-box">Email
    <span class="send"><svg width="20" height="20" viewBox="0 0 24 24" fill="#fdfdfd"><path d="M2 21l21-9L2 3v7l15 2-15 2z"/></svg></span>
  </div>
</div>
<div class="abs bottom-bar">
  <span>Copyright © <strong>MERIDIAN LEDGER</strong> - 2018 . All Right Reserved</span>
  <div class="social"><span></span><span></span><span></span></div>
</div>

</body>
</html>
```